Web Design Project (Mente Lumo)

We are going to do a therapy template to a psychologist. The site already exists, adress: www.mentelumo.net. So, its a total redesign job. I'm from Brazil, the language is PT-BR, so I'm gonna translate what you think be necessary. You can use the current structure from the website as a base to the new design. Check this template to see what I usually like: http://www.layoutkiosk.example/demo/51937.html
Updates

I'm waiting for new creative designs. The 'structure' image is just for 'pb'.

Requirements
Must have
• We need a modern menu, it should use a cool font style and make some kind of effect and little noise when the user pass over with the mouse (FLASH/HTML 5). The main page must emphasize the fact that we offer online treatment, like a picture or frame saying "Online Treatment, click here". It must also show the therapist picture and her name. The colors need to pass a tranquility feeling. The clinic telephone must always be present, doesn't matter which page the user is. The website must adapt to any resolution above 1024x768, crossbrowsing and accept javascript (I'll use www.agendrix.example, so its necessary embed code)
Nice to have
• I would appreciate if there was some kind of slow background animation, passing behind the text using the transparency.
Should not have
• Can't take too long to load, and won't have news or blog

```html
<!DOCTYPE html>
<html lang="pt-BR">
<head>
<meta charset="utf-8">
<title>Mente Lumo</title>
<link href="https://fonts.googleapis.com/css2?family=Arimo:wght@400;700&display=swap" rel="stylesheet">
<style>
:root{
  --header-top:#6f9bd0;
  --header-bottom:#3d6ea9;
  --logo-bg-top:#2a3a50;
  --logo-bg-bottom:#141c28;
  --logo-text:#a9cf6e;
  --hero-side:#d3e0ee;
  --hero-panel:#ebebeb;
  --heading-blue:#3f6fa8;
  --hero-text:#1d6e86;
  --accent-green:#84c31c;
  --body-text:#444;
  --rule:#c9c9c9;
  --btn-top:#79a3d4;
  --btn-bottom:#3f6fae;
  --footer-top:#415e80;
  --footer-bottom:#25466f;
  --white:#fff;
}
*{margin:0;padding:0;box-sizing:border-box}
html,body{width:1012px;height:1200px;overflow:hidden;background:var(--white);font-family:"Arimo",Arial,sans-serif}
.page{position:relative;width:1020px;height:1210px;transform:scale(.9922,.9917);transform-origin:0 0}
.site-header{position:absolute;left:0;top:0;width:1020px;height:140px;background:linear-gradient(var(--header-top),var(--header-bottom))}
.brand{position:absolute;left:40px;top:0;width:180px;height:140px;background:linear-gradient(var(--logo-bg-top),var(--logo-bg-bottom));display:flex;align-items:center;justify-content:center;gap:8px}
.brand-dot{width:14px;height:14px;border-radius:50%;background:var(--logo-text)}
.brand-name{color:var(--logo-text);font-weight:700;font-size:22px}
.phones{position:absolute;left:525px;top:28px;display:flex;gap:36px}
.phone{display:flex;align-items:center;gap:5px;color:var(--white);font-weight:700;font-size:14px;text-shadow:0 1px 1px rgba(0,0,0,.4)}
.main-nav{position:absolute;left:240px;top:65px;display:flex;align-items:flex-end;height:75px}
.main-nav a{color:var(--white);text-decoration:none;font-weight:700;font-size:15px;text-shadow:0 1px 1px rgba(0,0,0,.45);padding:0 13px 16px;position:relative;white-space:nowrap}
.main-nav a+a::before{content:"";position:absolute;left:-2px;top:9px;width:3px;height:3px;background:#b8d0ec}
.main-nav a.current{background:linear-gradient(#f4f4f4,#dcdcdc);color:#444;text-shadow:none;height:75px;padding:42px 5px 16px;border-radius:4px 4px 0 0;margin-right:8px}
.hero{position:absolute;left:0;top:140px;width:1020px;height:400px;background:var(--hero-side)}
.hero-panel{position:absolute;left:40px;top:0;width:940px;height:400px;background:var(--hero-panel)}
.hero-title{position:absolute;left:110px;top:75px;font-size:27px;font-weight:400;color:var(--heading-blue)}
.hero-title strong{color:var(--accent-green);font-size:31px}
.hero-text{position:absolute;left:111px;top:141px;width:400px;font-size:14.5px;line-height:20px;color:var(--hero-text)}
.btn{display:inline-block;background:linear-gradient(var(--btn-top),var(--btn-bottom));color:var(--white);font-weight:700;text-decoration:none;text-shadow:0 1px 1px rgba(0,0,0,.4);text-align:center;white-space:nowrap}
.hero .btn{position:absolute;left:111px;top:241px;width:149px;height:31px;line-height:31px;font-size:19px}
.slider-dots{position:absolute;left:109px;top:335px;display:flex;gap:5px}
.slider-dots span{width:20px;height:20px;border-radius:50%;background:radial-gradient(circle at 40% 30%,#7fa9de,#2b5c9c)}
.slider-dots span.active{background:radial-gradient(circle at 40% 30%,#c8f06a,#5d9d0c)}
.hero-photo{position:absolute;left:555px;top:25px;width:290px;height:375px;border-radius:120px 120px 0 0;background:linear-gradient(#4a4a4a,#9a9a9a)}
.section-title{position:absolute;top:576px;font-size:28px;font-weight:700;color:var(--accent-green)}
.rule{position:absolute;height:1px;background:var(--rule)}
.sub-title{font-size:17px;font-weight:700;color:var(--heading-blue)}
.topics{position:absolute;left:73px;top:666px}
.topic-cols{display:flex;margin-top:31px;margin-left:10px}
.topic-cols ul{list-style:none;width:138px}
.topic-cols li{font-size:12.5px;color:var(--body-text);height:27px;display:flex;align-items:flex-start;gap:10px}
.topic-cols li::before{content:"";width:11px;height:11px;border-radius:50%;background:radial-gradient(circle at 40% 35%,#eee,#9a9a9a);margin-top:1px;flex:none}
.feature-photo{position:absolute;left:433px;top:667px;width:120px;height:147px;background:linear-gradient(#6d6d6d,#cfcfcf)}
.feature{position:absolute;left:580px;top:666px;width:370px}
.feature .caps{font-size:14px;color:#333;margin-top:4px}
.feature p{font-size:13.5px;line-height:19px;color:var(--body-text);margin:23px 0 14px 2px;width:360px}
.small-btn{width:100px;height:21px;line-height:21px;font-size:14px}
.feature .small-btn{margin-left:3px}
.teaser{position:absolute;top:901px;width:220px}
.teaser p{font-size:13.5px;line-height:19px;color:var(--body-text);margin:10px 0 12px 1px}
.divider-v{position:absolute;left:687px;top:892px;width:1px;height:150px;background:var(--rule)}
.site-footer{position:absolute;left:0;top:1070px;width:1020px;height:140px;background:linear-gradient(var(--footer-top),var(--footer-bottom));color:var(--white);font-size:11.5px;line-height:14px;text-align:center;padding-top:45px}
</style>
</head>
<body>
<div class="page">
  <header class="site-header">
    <div class="brand"><span class="brand-dot"></span><span class="brand-name">Mente Lumo</span></div>
    <div class="phones">
      <span class="phone"><svg width="28" height="22" viewBox="0 0 28 22"><path d="M2 8c0-5 24-5 24 0v2h-6V8H8v2H2z" fill="#fff"/><path d="M6 11h16l3 9H3z" fill="#fff"/><circle cx="14" cy="15" r="3" fill="#4a7bb5"/></svg>(11) 4050-1123</span>
      <span class="phone"><svg width="18" height="24" viewBox="0 0 18 24"><rect x="1" y="1" width="16" height="22" rx="2" fill="#fff"/><rect x="4" y="4" width="10" height="6" fill="#4a7bb5"/><g fill="#4a7bb5"><rect x="4" y="12" width="2.5" height="2"/><rect x="8" y="12" width="2.5" height="2"/><rect x="12" y="12" width="2.5" height="2"/><rect x="4" y="16" width="2.5" height="2"/><rect x="8" y="16" width="2.5" height="2"/><rect x="12" y="16" width="2.5" height="2"/></g></svg>(11) 9818-2740</span>
      <span class="phone"><svg width="18" height="24" viewBox="0 0 18 24"><rect x="1" y="1" width="16" height="22" rx="2" fill="#fff"/><rect x="4" y="4" width="10" height="6" fill="#4a7bb5"/><g fill="#4a7bb5"><rect x="4" y="12" width="2.5" height="2"/><rect x="8" y="12" width="2.5" height="2"/><rect x="12" y="12" width="2.5" height="2"/><rect x="4" y="16" width="2.5" height="2"/><rect x="8" y="16" width="2.5" height="2"/><rect x="12" y="16" width="2.5" height="2"/></g></svg>(11) 7365-4418</span>
    </div>
    <nav class="main-nav">
      <a class="current" href="#">Home</a>
      <a href="#">Atendimento Online</a>
      <a href="#">Tratamentos</a>
      <a href="#">Perguntas</a>
      <a href="#">Consultório</a>
      <a href="#">Localização</a>
      <a href="#">Contato</a>
    </nav>
  </header>

  <section class="hero">
    <div class="hero-panel">
      <h1 class="hero-title">Atendimento <strong>ONLINE</strong></h1>
      <p class="hero-text">Faça sua terapia de onde estiver, com sigilo e segurança. Sessões por vídeo em horários flexíveis, com o mesmo cuidado do consultório. Agende a sua primeira conversa.</p>
      <a class="btn" href="#">Clique aqui</a>
      <div class="slider-dots"><span></span><span class="active"></span><span></span><span></span></div>
      <div class="hero-photo" role="img" aria-label="Black and white portrait of the therapist Dra. Helena Martins"></div>
    </div>
  </section>

  <h2 class="section-title" style="left:65px">Tratamentos</h2>
  <h2 class="section-title" style="left:431px">Sua Psicóloga</h2>
  <div class="rule" style="left:40px;top:632px;width:940px"></div>

  <section class="topics">
    <h3 class="sub-title">Áreas de atendimento</h3>
    <div class="topic-cols">
      <ul style="width:143px"><li>Ansiedade</li><li>Depressão</li><li>Estresse</li><li>Pânico</li><li>Fobias</li><li>Luto</li><li>Insônia</li><li>Autoestima</li><li>Timidez</li><li>Ciúme</li><li>Traumas</li><li>Compulsões</li></ul>
      <ul style="width:180px"><li>Terapia de Casal</li><li>Terapia Familiar</li><li>Orientação Vocacional</li><li>Orientação de Pais</li><li>Adolescentes</li><li>Conflitos no Trabalho</li><li>Terapia Individual</li><li>Relacionamentos</li><li>Mudanças de Vida</li><li>Gestação e Maternidade</li><li>Idosos e Cuidadores</li><li>Atendimento Online</li></ul>
    </div>
  </section>

  <div class="feature-photo" role="img" aria-label="Black and white photo of the therapist"></div>
  <article class="feature">
    <h3 class="sub-title">Dra. Helena Martins</h3>
    <div class="caps">PSICÓLOGA CLÍNICA E TERAPEUTA DE CASAIS</div>
    <p>Há mais de quinze anos acolho pessoas em busca de equilíbrio, no consultório e também por atendimento online.</p>
    <a class="btn small-btn" href="#">Saiba mais</a>
  </article>
  <div class="rule" style="left:431px;top:860px;width:500px"></div>

  <article class="teaser" style="left:432px">
    <h3 class="sub-title">Terapia Online</h3>
    <p>Sessões por vídeo com total sigilo, para você cuidar da mente sem sair de casa.</p>
    <a class="btn small-btn" href="#">Saiba mais</a>
  </article>
  <div class="divider-v"></div>
  <article class="teaser" style="left:732px">
    <h3 class="sub-title">Consultório</h3>
    <p>Um espaço tranquilo e reservado, pensado para o seu conforto em cada sessão.</p>
    <a class="btn small-btn" href="#">Saiba mais</a>
  </article>

  <footer class="site-footer">
    Mente Lumo · Psicologia e atendimento online.<br>
    Atendimento presencial e por vídeo, de segunda a sábado, com hora marcada. Ligue e agende<br>
    sua consulta.
  </footer>
</div>
</body>
</html>
```